Create company sales sheet to increase referrals so we can get new products

Create a 1 page sales sheet based on the text and logo that we provided.

We are a distribution company. Product manufacturer are a great source of leads for us - as they talk to our potential clients, eg., owners of medical projects, and we are hoping to get referrals.

Keep equal emphasis on each of the trhee words of "Bluefern Carrier Group.

Manufacturers of medical products

It Company

• Equal emphasis on "Bluefern Carrier Group"
• We are expecting a one page one side, but if it looks better, you can make it go to a second page (or double sided)

```html
<!DOCTYPE html>
<html lang="en">
<head>
<meta charset="utf-8">
<title>Bluefern Carrier Group – Sales Sheet</title>
<link href="https://fonts.googleapis.com/css2?family=Roboto+Condensed:wght@400;700&family=Cabin:wght@400;500&family=Montserrat:wght@500;600&display=swap" rel="stylesheet">
<style>
  :root {
    --red: #c20b22;
    --red-dark: #9c0716;
    --red-deep: #7e0412;
    --ink: #1c1c1c;
    --body: #2b2b2b;
    --paper: #f4f4f4;
    --backdrop: #e6e5e3;
    --white: #ffffff;
  }
  * { box-sizing: border-box; margin: 0; padding: 0; }
  html, body { width: 1200px; height: 1200px; overflow: hidden; background: var(--backdrop); }
  .sheet {
    position: absolute; left: 170px; top: 20px;
    width: 860px; height: 1160px;
    background: linear-gradient(180deg, #fafafa 0%, var(--paper) 100%);
    overflow: hidden;
    box-shadow: 0 4px 18px rgba(0,0,0,.12);
  }
  .header-shape, .footer-shape { position: absolute; left: 0; width: 860px; }
  .header-shape { top: 0; height: 330px; }
  .footer-shape { bottom: 0; height: 212px; }

  .tagline {
    position: absolute; top: 52px; left: 0; width: 860px; text-align: center;
    font-family: "Montserrat", sans-serif; font-weight: 500;
    font-size: 22px; letter-spacing: 2px; color: var(--white);
  }
  .questions { position: absolute; top: 122px; left: 56px; width: 720px; list-style: none; }
  .questions li {
    display: flex; gap: 12px; align-items: flex-start; margin-bottom: 22px;
    font-family: "Roboto Condensed", sans-serif; font-weight: 700;
    font-size: 15.5px; letter-spacing: 1px; line-height: 1.4; color: var(--white);
  }
  .questions svg { flex: none; width: 34px; height: 34px; margin-top: 2px; }

  .brand-card {
    position: absolute; top: 240px; left: 400px; width: 270px; height: 118px;
    background: var(--white); box-shadow: 0 6px 14px rgba(0,0,0,.25);
    display: flex; flex-direction: column; align-items: center; justify-content: center; gap: 12px;
  }
  .brand-card .mark { width: 34px; height: 34px; border-radius: 50%; background: var(--red); }
  .brand-card .name {
    font-family: "Roboto Condensed", sans-serif; font-weight: 700;
    font-size: 19px; letter-spacing: .5px; color: var(--ink);
  }

  .content { position: absolute; top: 388px; left: 62px; width: 740px; }
  .content h1 {
    font-family: "Roboto Condensed", sans-serif; font-weight: 700;
    font-size: 32px; letter-spacing: 1px; color: var(--red); margin-bottom: 10px;
  }
  .intro {
    font-family: "Cabin", sans-serif; font-size: 15.5px; line-height: 1.5;
    color: var(--body); margin-bottom: 22px;
  }
  .point { margin: 0 0 20px 14px; }
  .point:last-child { margin-bottom: 0; }
  .point h2 {
    display: flex; align-items: center; gap: 10px;
    font-family: "Roboto Condensed", sans-serif; font-weight: 700;
    font-size: 20px; color: var(--ink); margin-bottom: 6px;
  }
  .point h2 .chevrons { color: var(--red); font-size: 22px; letter-spacing: -3px; }
  .point p {
    margin-left: 28px; width: 640px;
    font-family: "Cabin", sans-serif; font-size: 14px; line-height: 1.55; color: var(--body);
  }

  .closing {
    position: absolute; left: 50px; bottom: 44px;
    font-family: "Roboto Condensed", sans-serif; font-weight: 700;
    font-size: 24px; line-height: 1.18; letter-spacing: 1px; color: var(--white);
  }
  .contact-tab {
    position: absolute; right: 140px; bottom: 186px;
    background: var(--white); padding: 8px 26px; box-shadow: 0 3px 8px rgba(0,0,0,.25);
    font-family: "Roboto Condensed", sans-serif; font-weight: 700; font-size: 20px;
    letter-spacing: 1px; color: var(--red);
  }
  .contact { position: absolute; left: 520px; bottom: 30px; list-style: none; color: var(--white); }
  .contact li { display: flex; gap: 10px; align-items: flex-start; margin-bottom: 12px; font-family: "Cabin", sans-serif; font-size: 14.5px; line-height: 1.45; }
  .contact li.phone { font-family: "Roboto Condensed", sans-serif; font-weight: 700; font-size: 19px; }
  .contact svg { flex: none; width: 14px; height: 14px; margin-top: 4px; }
</style>
</head>
<body>
<main class="sheet">
  <svg class="header-shape" viewBox="0 0 860 330" preserveAspectRatio="none" aria-hidden="true">
    <defs>
      <linearGradient id="headerRed" x1="0" y1="0" x2="1" y2="1">
        <stop offset="0" stop-color="#d0112a"/>
        <stop offset="1" stop-color="#b20a1e"/>
      </linearGradient>
    </defs>
    <polygon points="0,0 860,0 860,270 660,300 400,310 0,255" fill="url(#headerRed)"/>
    <polygon points="0,255 400,310 400,318 0,262" fill="var(--red-deep)"/>
    <polygon points="660,300 860,260 860,272 660,312" fill="var(--red-deep)"/>
    <rect x="0" y="36" width="860" height="62" fill="var(--red-dark)" opacity=".75"/>
  </svg>

  <p class="tagline">WE GIVE NEW MEDICAL PRODUCT INNOVATORS A CHANCE.</p>

  <ul class="questions">
    <li>
      <svg viewBox="0 0 34 34" aria-hidden="true"><circle cx="16" cy="16" r="13" fill="none" stroke="#fff" stroke-width="3"/><path d="M11.5 12.5a4.5 4.5 0 1 1 6.5 4c-1.3.7-2 1.6-2 3" fill="none" stroke="#fff" stroke-width="2.6" stroke-linecap="round"/><circle cx="16" cy="23.5" r="1.7" fill="#fff"/><path d="M25 26l6 6" stroke="#fff" stroke-width="3.4" stroke-linecap="round"/></svg>
      <span>DO YOU HAVE EFFECTIVE PRODUCTS WITH LOW SALES NUMBERS IN NEED OF A DISTRIBUTION PARTNER?</span>
    </li>
    <li>
      <svg viewBox="0 0 34 34" aria-hidden="true"><circle cx="16" cy="16" r="13" fill="none" stroke="#fff" stroke-width="3"/><path d="M11.5 12.5a4.5 4.5 0 1 1 6.5 4c-1.3.7-2 1.6-2 3" fill="none" stroke="#fff" stroke-width="2.6" stroke-linecap="round"/><circle cx="16" cy="23.5" r="1.7" fill="#fff"/><path d="M25 26l6 6" stroke="#fff" stroke-width="3.4" stroke-linecap="round"/></svg>
      <span>DO YOU HAVE CUSTOMERS WITH INNOVATIVE PRODUCTS THAT NEED DISTRIBUTION SERVICES?</span>
    </li>
  </ul>

  <div class="brand-card">
    <span class="mark" aria-hidden="true"></span>
    <span class="name">BLUEFERN CARRIER GROUP</span>
  </div>

  <section class="content">
    <h1>BLUEFERN CARRIER GROUP CAN HELP!</h1>
    <p class="intro">Increase your production volume by assisting your customers with product distribution. We will distribute your customers' promising new products with strategic launch analysis, comprehensive targeted marketing programs, and global fulfillment and distribution services, at no cost to manufacturers. Bluefern Carrier Group (BCG) specializes in launching new medical products by partnering with medical innovators in bringing new and next generation medical technologies to market.</p>

    <article class="point">
      <h2><span class="chevrons">››</span>Grow your Manufacturing Enterprise into a Manufacturing Powerhouse</h2>
      <p>Enlighten your customers about BCG and increase manufacturing volumes, as well as earning customer appreciation, loyalty, and referrals.</p>
    </article>
    <article class="point">
      <h2><span class="chevrons">››</span>Our Focus</h2>
      <p>We are especially interested in technologies that improve patient care, prevent injury or illness, reduce or mitigate disabilities, save lives, and/or decrease healthcare costs. We look for technologies supported by clinical studies and evidence-based practices.</p>
    </article>
    <article class="point">
      <h2><span class="chevrons">››</span>Distribution and Product Launch Support</h2>
      <p>BCG handles all aspects of distribution, product launch, marketing, and sales. We execute creative and effective product launch strategies, using customer motivation psychology combined with targeted and comprehensive client materials, experienced sales force, and extensive global distribution channels.</p>
    </article>
  </section>

  <svg class="footer-shape" viewBox="0 0 860 230" preserveAspectRatio="none" aria-hidden="true">
    <path d="M300 40 L860 12 L860 230 L440 230 C410 150 370 80 300 40 Z" fill="var(--red)"/>
    <path d="M0 0 C170 0 360 60 450 230 L0 230 Z" fill="#d8d8d8"/>
    <path d="M0 8 C170 8 350 70 435 230 L0 230 Z" fill="#111"/>
  </svg>

  <p class="closing">ASSIST YOUR<br>CLIENTS AND INCREASE<br>YOUR MANUFACTURING<br>VOLUME AND PROFITS</p>

  <div class="contact-tab">CONTACT US</div>
  <ul class="contact">
    <li>
      <svg viewBox="0 0 14 14" aria-hidden="true"><path d="M7 1a4 4 0 0 1 4 4c0 3-4 8-4 8S3 8 3 5a4 4 0 0 1 4-4z" fill="none" stroke="#fff" stroke-width="1.5"/><circle cx="7" cy="5" r="1.4" fill="#fff"/></svg>
      <span>Bluefern Carrier Group, 4870<br>Harbor Line Road, Dover, DE 19901</span>
    </li>
    <li class="phone">
      <svg viewBox="0 0 14 14" aria-hidden="true"><path d="M3 1.5l2 .3.8 2.6-1.4 1.1a7 7 0 0 0 4 4l1.1-1.4 2.6.8.3 2c-.3.9-1.2 1.4-2.2 1.3A10 10 0 0 1 1.4 3.7C1.3 2.7 1.9 1.8 3 1.5z" fill="#fff"/></svg>
      <span>302.555.0148</span>
    </li>
    <li>
      <svg viewBox="0 0 14 14" aria-hidden="true"><circle cx="7" cy="7" r="5.5" fill="none" stroke="#fff" stroke-width="1.3"/><path d="M1.5 7h11M7 1.5c-2.5 3-2.5 8 0 11M7 1.5c2.5 3 2.5 8 0 11" fill="none" stroke="#fff" stroke-width="1.1"/></svg>
      <span>www.bluefern-carriergroup.com</span>
    </li>
  </ul>
</main>
</body>
</html>
```